I need the below text put into an illustration/high res image so I can print out and frame and give to my fiance. Can be simple but must look elegant. Idea is that the text can be written in the sand on the attached pics (let me know if you require more high res). Not precious on the dimensions but think no more than 90cm length or width. Can be smaller whatever you think works best. You can half long sentences if you think it will look better.
Update: some of you asked for a picture of us, not sure it works but have attached one
Marriage
Marriage isn’t for you.
You don’t marry to make yourself happy, you marry to make someone else happy.
More than that, your marriage isn’t for yourself, you’re marrying for a family.
Not just for the in-laws and all of that nonsense, but for your future children.
Who do you want to help you raise them?
Who do you want to influence them?
Marriage isn’t for you.
It’s not about you.
Marriage is about the person you married.

```html
<!DOCTYPE html>
<html lang="en">
<head>
<meta charset="utf-8">
<title>Marriage</title>
<link rel="stylesheet" href="https://fonts.googleapis.com/css2?family=Yellowtail&family=Dancing+Script:wght@500&display=swap">
<style>
  :root {
    --sky-haze: #f7ecd6;
    --sky-pink: #f3d6d2;
    --sky-blue: #8fc2d6;
    --headland: #6f8f94;
    --sea: #7fb6c4;
    --surf: #d9ebee;
    --wet-sand: #f1e3bd;
    --sand-light: #eec27a;
    --sand: #e2a44c;
    --sand-deep: #d08c3a;
    --glow: rgba(255, 251, 232, 0.9);
    --gold-flourish: rgba(255, 238, 160, 0.35);
    --rose-tone: rgba(120, 90, 50, 0.22);
    --ink: rgba(38, 24, 12, 0.88);
  }
  html, body {
    margin: 0;
    padding: 0;
    width: 1200px;
    height: 960px;
    overflow: hidden;
    background: var(--sand);
  }
  .canvas {
    position: relative;
    width: 1200px;
    height: 960px;
    overflow: hidden;
  }
  .beach-scene {
    position: absolute;
    inset: 0;
    background:
      radial-gradient(ellipse 360px 260px at 110px 60px, var(--glow), transparent 72%),
      linear-gradient(168deg, rgba(255, 248, 225, 0.75) 0%, rgba(255, 248, 225, 0.55) 25%, transparent 42%),
      linear-gradient(180deg,
        var(--sky-haze) 0%,
        var(--sky-pink) 4%,
        var(--sky-blue) 7.5%,
        var(--headland) 8.5%,
        var(--sea) 9.5%,
        var(--surf) 12.5%,
        var(--wet-sand) 15%,
        var(--sand-light) 26%,
        var(--sand) 58%,
        var(--sand-deep) 100%);
  }
  .flourish {
    position: absolute;
  }
  .flourish--top {
    left: 690px; top: 170px; width: 400px; height: 140px;
    background: radial-gradient(closest-side, var(--gold-flourish), transparent);
  }
  .flourish--left {
    left: 0; top: 450px; width: 440px; height: 300px;
    background: radial-gradient(closest-side, var(--gold-flourish), transparent);
  }
  .flourish--right {
    left: 600px; top: 450px; width: 600px; height: 510px;
    background: radial-gradient(closest-side, var(--gold-flourish), transparent);
  }
  .rose {
    position: absolute;
    left: 290px; top: 780px; width: 220px; height: 100px;
    background: radial-gradient(closest-side, var(--rose-tone), transparent);
  }
  .poem {
    margin: 0;
    padding: 0;
    list-style: none;
  }
  .poem__line {
    position: absolute;
    margin: 0;
    white-space: nowrap;
    line-height: 1;
    font-weight: 400;
    font-family: "Yellowtail", "Dancing Script", cursive;
    color: var(--ink);
  }
  .poem__title { left: 512px; top: 232px; font-size: 16px; }
  .l1  { left: 500px; top: 270px; font-size: 19px; }
  .l2  { left: 487px; top: 312px; font-size: 21px; }
  .l3  { left: 474px; top: 358px; font-size: 22px; }
  .l4  { left: 459px; top: 405px; font-size: 23px; }
  .l5  { left: 443px; top: 454px; font-size: 25px; }
  .l6  { left: 426px; top: 510px; font-size: 27px; }
  .l7  { left: 408px; top: 573px; font-size: 29px; }
  .l8  { left: 386px; top: 638px; font-size: 31px; }
  .l9  { left: 366px; top: 712px; font-size: 33px; }
</style>
</head>
<body>
<main class="canvas">
  <div class="beach-scene" role="img" aria-label="Photograph of a golden sandy beach at sunset with waves, a distant headland and sun flares"></div>
  <div class="flourish flourish--top" role="img" aria-label="Gold decorative flourish ornament"></div>
  <div class="flourish flourish--left" role="img" aria-label="Gold decorative flourish ornament"></div>
  <div class="flourish flourish--right" role="img" aria-label="Gold decorative flourish ornament"></div>
  <div class="rose" role="img" aria-label="A single white rose lying on the sand"></div>

  <h1 class="poem__line poem__title">Marriage</h1>
  <ul class="poem">
    <li class="poem__line l1">Marriage isn’t for you.</li>
    <li class="poem__line l2">You don’t marry to make yourself happy, you marry to make someone else happy.</li>
    <li class="poem__line l3">More than that, your marriage isn’t for yourself, you’re marrying for a family.</li>
    <li class="poem__line l4">Not just for the in-laws and all of that nonsense, but for your future children.</li>
    <li class="poem__line l5">Who do you want to help you raise them?</li>
    <li class="poem__line l6">Who do you want to influence them?</li>
    <li class="poem__line l7">Marriage isn’t for you.</li>
    <li class="poem__line l8">It’s not about you.</li>
    <li class="poem__line l9">Marriage is about the person you married</li>
  </ul>
</main>
</body>
</html>
```